Musician looking for catchy Web Design for promotion

My name is Bridget Colfer. I'm an Irish musician who plays the tin whistle and the flute. I'm also the leader of a traditional Irish music and dance ensemble called Rowan Road Players (www.rowanroadplayers.test) and for the past 30 years, I've toured the world performing thousands of concerts. I run an annual cruise (www.bridgetcolfercruise.test) that I would like a link to, and I'm also I'm organizing tours to Ireland that I would like a page set up for. I'm looking for a website to promote my tours and my music.

Hello Graphic Designers, I am only looking for the design of the home page to make my decision. Thank you. Bridget

Target Market(s)

Music fans of Irlsh and World Music

Industry/Entity Type

Entertainment Industry

Number of Pages Required

5+ page

Requirements
Must have
• I'm looking for a catchy design that shows a photo of me. I would like a few links....
• BIO
• TOURDATES
• BRIDGET COLFER CRUISE
• MUSICAL TOUR OF IRELAND
• CONTACT
• VIDEO
• GALLERY
• CONTACT
• MAILING LIST
• STORE
Nice to have
• we'll see!

```html
<!DOCTYPE html>
<html lang="en">
<head>
<meta charset="utf-8">
<title>Bridget Colfer — Irish Flute &amp; Whistle</title>
<link href="https://fonts.googleapis.com/css2?family=Roboto:wght@300;400;500;700;900&display=swap" rel="stylesheet">
<style>
  :root {
    --ink: #1c1c1c;
    --text: #3a3a3a;
    --muted: #8d8d8d;
    --rule: #e3e3e3;
    --accent: #9a6a4a;
    --accent-soft: #c9a892;
    --white: #ffffff;
    --footer: #262626;
    --footer-text: #d8d8d8;
    --icon-grey: #4a4a4a;
  }
  * { box-sizing: border-box; margin: 0; padding: 0; }
  html, body { width: 1200px; height: 2826px; overflow: hidden; }
  body { position: relative; background: var(--white); font-family: "Roboto", sans-serif; color: var(--text); }
  a { color: inherit; text-decoration: none; }

  /* Header */
  .site-header { position: absolute; left: 0; top: 0; width: 1200px; height: 56px; background: var(--white); }
  .brand { position: absolute; left: 230px; top: 18px; display: flex; align-items: center; gap: 8px;
    font: 700 11px/1 "Roboto", sans-serif; color: var(--ink); letter-spacing: .5px; }
  .brand-dot { width: 14px; height: 14px; border-radius: 50%; background: var(--ink); }
  .main-nav { position: absolute; left: 604px; top: 23px; display: flex; gap: 18px;
    font: 700 9.5px/1 "Roboto", sans-serif; color: var(--ink); text-transform: uppercase; }

  /* Hero */
  .hero { position: absolute; left: 0; top: 56px; width: 1200px; height: 444px;
    background: linear-gradient(180deg, #1a120c 0%, #c9b27a 14%, #d8c596 26%, #8c3a1a 44%, #a9481f 62%, #6e2410 82%, #3c160b 100%); }
  .hero-title { position: absolute; left: 0; width: 1200px; top: 148px; text-align: center;
    font: 500 46px/1 "Roboto", sans-serif; letter-spacing: 4px; color: var(--white); }
  .hero-rule { position: absolute; left: 358px; width: 503px; height: 1px; background: rgba(255,255,255,.8); }
  .hero-copy { position: absolute; left: 364px; top: 230px; width: 494px;
    font: 400 11.5px/19px "Roboto", sans-serif; color: var(--white); letter-spacing: .9px; }
  .hero-arrow { position: absolute; top: 205px; }
  .scroll-mouse { position: absolute; left: 591px; top: 400px; }

  /* Section headings */
  .section-title { position: absolute; left: 0; width: 1200px; text-align: center;
    font: 700 21px/1 "Roboto", sans-serif; letter-spacing: 3px; color: var(--ink); }
  .title-bar { position: absolute; height: 8px; width: 80px;
    background: linear-gradient(90deg, rgba(220,220,220,0), var(--rule)); }
  .title-bar.right { background: linear-gradient(90deg, var(--rule), rgba(220,220,220,0)); }

  /* About */
  .bio-frame { position: absolute; border: 1px solid var(--accent-soft); }
  .bio-photo { position: absolute; background: linear-gradient(160deg, #c79b67 0%, #8a5a2e 45%, #2b1d14 100%); }
  .bio-photo.second { background: linear-gradient(150deg, #5b4a32 0%, #ada58e 40%, #2a1d1a 100%); }
  .bio-tab { position: absolute; height: 6px; background: var(--accent); }
  .bio-text { position: absolute; font: 400 11.5px/20px "Roboto", sans-serif; color: var(--text); letter-spacing: .5px; }
  .drop-cap { float: left; font: 400 42px/36px "Roboto", sans-serif; color: var(--ink); margin: 3px 5px 0 0; }
  .more-link { position: absolute; display: flex; align-items: center; gap: 8px;
    font: 500 13.5px/1 "Roboto", sans-serif; color: var(--accent); text-decoration: underline; }

  /* Gallery */
  .video { position: absolute; left: 273px; top: 1405px; width: 652px; height: 368px;
    background: linear-gradient(180deg, #d9c48f 0%, #b79a5c 10%, #8c3a1a 30%, #a9481f 55%, #6e2410 75%, #c8a860 88%, #3b2a18 100%); }
  .video-play { position: absolute; left: 292px; top: 163px; width: 70px; height: 48px; border-radius: 12px; background: #c4302b; opacity: .92; }
  .video-controls { position: absolute; left: 0; bottom: 0; width: 652px; height: 24px; background: rgba(0,0,0,.65); }
  .video-progress { position: absolute; left: 8px; right: 8px; top: 2px; height: 3px; background: rgba(255,255,255,.35); }
  .thumb { position: absolute; top: 1833px; height: 172px; }
  .carousel-arrow { position: absolute; top: 1906px; }

  /* Store */
  .track { position: absolute; left: 288px; width: 720px; height: 110px; }
  .track-art { position: absolute; left: 0; top: 0; width: 110px; height: 106px;
    background: linear-gradient(120deg, #a9481f 0%, #7a2a14 40%, #d9c48f 55%, #8c3a1a 70%, #5a1e0d 100%); }
  .track-play { position: absolute; left: 132px; top: 10px; width: 24px; height: 24px; border-radius: 50%; background: var(--accent); }
  .track-play::after { content: ""; position: absolute; left: 9px; top: 6px; border-left: 9px solid var(--white); border-top: 6px solid transparent; border-bottom: 6px solid transparent; }
  .track-artist { position: absolute; left: 166px; top: 10px; font: 400 8.5px/1 "Roboto", sans-serif; color: var(--muted); }
  .track-name { position: absolute; left: 166px; top: 24px; font: 400 8px/1 "Roboto", sans-serif; color: var(--muted); text-transform: uppercase; }
  .waveform { position: absolute; left: 132px; top: 38px; }
  .track-time { position: absolute; top: 82px; font: 400 8px/1 "Roboto", sans-serif; color: var(--muted); }
  .track-links { position: absolute; left: 132px; top: 92px; display: flex; gap: 20px;
    font: 500 13.5px/1 "Roboto", sans-serif; color: var(--accent); text-decoration: underline; }
  .price { position: absolute; left: 569px; top: 46px; font: 400 11px/1 "Roboto", sans-serif; color: var(--muted); }
  .buy { position: absolute; left: 572px; top: 64px; font: 500 17px/1 "Roboto", sans-serif; color: var(--accent); text-decoration: underline; }

  /* Footer */
  .site-footer { position: absolute; left: 0; top: 2632px; width: 1200px; height: 194px; background: var(--footer); color: var(--footer-text); }
  .site-footer .brand { left: 230px; top: 40px; color: var(--white); }
  .site-footer .brand-dot { background: var(--white); }
  .footer-col { position: absolute; list-style: none; font: 700 7.5px/13.5px "Roboto", sans-serif; text-transform: uppercase; color: var(--white); }
  .footer-col.light { font-weight: 400; color: var(--footer-text); }
  .footer-head { position: absolute; font: 700 7.5px/1 "Roboto", sans-serif; color: var(--white); text-transform: uppercase; }
  .social { position: absolute; left: 844px; top: 2688px; display: flex; gap: 10px; }
  .social span { width: 24px; height: 24px; border-radius: 50%; background: var(--icon-grey); }
  .copyright { position: absolute; left: 245px; top: 2798px; font: 400 7.5px/1 "Roboto", sans-serif; color: #8a8a8a; }
</style>
</head>
<body>

<header class="site-header">
  <a class="brand" href="#"><span class="brand-dot"></span>BRIDGET COLFER'S</a>
  <nav class="main-nav">
    <a href="#">Home</a><a href="#">About me</a><a href="#">Contact</a><a href="#">Tour dates ▾</a><a href="#">Bridget Colfer Cruise</a><a href="#">Gallery</a><a href="#">Store</a>
  </nav>
</header>

<section class="hero" role="img" aria-label="Open instrument roll holding rows of tin whistles and flutes in red fabric sleeves">
  <div class="hero-rule" style="top:142px"></div>
  <h1 class="hero-title">TOURS OF IRELAND</h1>
  <div class="hero-rule" style="top:202px"></div>
  <p class="hero-copy">Contrary to popular belief, Lorem Ipsum is not simply random text. It has roots in a piece of classical Latin literature from 45 BC, making it over 2000 years old. Martin Oakes, a Latin professor at Larchfield College in Virginia, looked up one of the more obscure Latin words, consectetur, from</p>
  <svg class="hero-arrow" style="left:112px" width="28" height="54" viewBox="0 0 28 54"><path d="M28 0 L0 27 L28 54 Z" fill="rgba(255,255,255,.8)"/></svg>
  <svg class="hero-arrow" style="left:1076px" width="28" height="54" viewBox="0 0 28 54"><path d="M0 0 L28 27 L0 54 Z" fill="rgba(255,255,255,.8)"/></svg>
  <svg class="scroll-mouse" width="18" height="28" viewBox="0 0 18 28"><rect x="1" y="1" width="16" height="26" rx="8" fill="none" stroke="#fff" stroke-width="1.6"/><rect x="8" y="6" width="2" height="6" rx="1" fill="#fff"/></svg>
</section>

<!-- About -->
<div class="title-bar" style="left:448px;top:541px"></div>
<h2 class="section-title" style="top:533px">ABOUT ME</h2>
<div class="title-bar right" style="left:674px;top:541px"></div>

<div class="bio-frame" style="left:241px;top:586px;width:622px;height:205px"></div>
<div class="bio-tab" style="left:618px;top:613px;width:64px"></div>
<div class="bio-photo" style="left:652px;top:603px;width:230px;height:298px" role="img" aria-label="Portrait of Bridget Colfer in black holding a flute"></div>
<p class="bio-text" style="left:258px;top:604px;width:330px"><span class="drop-cap">B</span>RIDGET COLFER is a much-loved flute and whistle player known across Irish music circles in America. She was born in Boston, Massachusetts to Irish parents, and she is the third of six children raised in a musical household. Her mother Maura hails from Kilbrannagh, County Kerry and her father Declan, a well-known concertina player, was a native of Drumcarra, County Sligo.</p>

<div class="bio-frame" style="left:335px;top:953px;width:626px;height:208px"></div>
<div class="bio-photo second" style="left:273px;top:972px;width:232px;height:302px" role="img" aria-label="Bridget Colfer smiling outdoors beside a carved wooden post"></div>
<div class="bio-tab" style="left:471px;top:996px;width:66px"></div>
<p class="bio-text" style="left:599px;top:967px;width:352px"><span class="drop-cap">B</span>ridget heard traditional Irish music early in her life, listening to her father and his friends play tunes at family gatherings and social evenings. She began taking lessons from local flutist Tom Carrick, and within a few short years she was winning regional titles on both the concert flute and tin whistle. In 1991, Bridget took first place at the Northern Feis on the whistle.</p>
<a class="more-link" href="#" style="left:731px;top:1250px">Read more <svg width="34" height="10" viewBox="0 0 34 10"><path d="M0 5 H32 M27 1 L32 5 L27 9" fill="none" stroke="#c9a892" stroke-width="1.2"/></svg></a>

<!-- Gallery -->
<div class="title-bar" style="left:448px;top:1351px"></div>
<h2 class="section-title" style="top:1343px">GALLERY</h2>
<div class="title-bar right" style="left:674px;top:1351px"></div>

<div class="video" role="img" aria-label="Video still of flutes and whistles laid in an instrument roll">
  <div class="video-play"><svg width="70" height="48" viewBox="0 0 70 48"><path d="M28 14 L46 24 L28 34 Z" fill="#fff"/></svg></div>
  <div class="video-controls">
    <div class="video-progress"></div>
    <svg width="652" height="24" viewBox="0 0 652 24"><path d="M10 10 L17 14 L10 18 Z" fill="#fff"/><path d="M28 10 L33 14 L28 18 Z M33 10 H35 V18 H33 Z" fill="#fff"/><path d="M46 12 H49 L53 9 V19 L49 16 H46 Z" fill="#fff"/><rect x="610" y="10" width="12" height="8" fill="none" stroke="#fff"/><rect x="630" y="10" width="12" height="8" fill="none" stroke="#fff"/></svg>
  </div>
</div>

<svg class="carousel-arrow" style="left:196px" width="14" height="26" viewBox="0 0 14 26"><path d="M14 0 L0 13 L14 26 Z" fill="#d6d6d6"/></svg>
<div class="thumb" style="left:226px;width:249px;background:linear-gradient(180deg,#c9d3d8 0%,#8aa0ad 35%,#5c7a3c 70%,#3a4a2a 100%)" role="img" aria-label="Bridget Colfer playing whistle on a coastal clifftop"></div>
<div class="thumb" style="left:475px;width:252px;background:linear-gradient(135deg,#4a1e12 0%,#b0704a 45%,#6a3520 100%)" role="img" aria-label="Close-up of hands on a wooden flute"></div>
<div class="thumb" style="left:727px;width:249px;background:linear-gradient(180deg,#5a2a1a 0%,#2a1410 50%,#6b3a22 100%)" role="img" aria-label="The Rowan Road Players on stage with instruments"></div>
<svg class="carousel-arrow" style="left:998px" width="14" height="26" viewBox="0 0 14 26"><path d="M0 0 L14 13 L0 26 Z" fill="#d6d6d6"/></svg>

<a class="more-link" href="#" style="left:560px;top:2050px">See more <svg width="34" height="10" viewBox="0 0 34 10"><path d="M0 5 H32 M27 1 L32 5 L27 9" fill="none" stroke="#c9a892" stroke-width="1.2"/></svg></a>

<!-- Store -->
<div class="title-bar" style="left:448px;top:2121px"></div>
<h2 class="section-title" style="top:2113px">STORE</h2>
<div class="title-bar right" style="left:674px;top:2121px"></div>

<svg width="0" height="0" style="position:absolute">
  <defs>
    <pattern id="wave" width="36" height="36" patternUnits="userSpaceOnUse">
      <rect x="0" y="14" width="2" height="22" fill="#c8c8c8"/><rect x="4" y="8" width="2" height="28" fill="#c8c8c8"/>
      <rect x="8" y="18" width="2" height="18" fill="#c8c8c8"/><rect x="12" y="4" width="2" height="32" fill="#c8c8c8"/>
      <rect x="16" y="12" width="2" height="24" fill="#c8c8c8"/><rect x="20" y="20" width="2" height="16" fill="#c8c8c8"/>
      <rect x="24" y="6" width="2" height="30" fill="#c8c8c8"/><rect x="28" y="16" width="2" height="20" fill="#c8c8c8"/>
      <rect x="32" y="10" width="2" height="26" fill="#c8c8c8"/>
    </pattern>
  </defs>
</svg>

<div class="track" style="top:2176px">
  <div class="track-art" role="img" aria-label="Tin whistle on red fabric"></div>
  <span class="track-play"></span><span class="track-artist">Bridget Colfer</span><span class="track-name">Some song</span>
  <svg class="waveform" width="392" height="38"><rect width="392" height="36" fill="url(#wave)"/><rect y="36" width="392" height="1" fill="#999"/></svg>
  <span class="track-time" style="left:132px">0:00</span><span class="track-time" style="left:508px">0:02</span>
  <div class="track-links"><a href="#">Download demo</a><a href="#">Share</a></div>
  <span class="price">0.99 c</span><a class="buy" href="#">Buy</a>
</div>

<div class="track" style="top:2317px">
  <div class="track-art" role="img" aria-label="Tin whistle on red fabric"></div>
  <span class="track-play"></span><span class="track-artist">Bridget Colfer</span><span class="track-name">Some song</span>
  <svg class="waveform" width="392" height="38"><rect width="392" height="36" fill="url(#wave)"/><rect y="36" width="392" height="1" fill="#999"/></svg>
  <span class="track-time" style="left:132px">0:00</span><span class="track-time" style="left:508px">0:02</span>
  <div class="track-links"><a href="#">Download demo</a><a href="#">Share</a></div>
  <span class="price">0.99 c</span><a class="buy" href="#">Buy</a>
</div>

<div class="track" style="top:2464px">
  <div class="track-art" role="img" aria-label="Tin whistle on red fabric"></div>
  <span class="track-play"></span><span class="track-artist">Bridget Colfer</span><span class="track-name">Some song</span>
  <svg class="waveform" width="392" height="38"><rect width="392" height="36" fill="url(#wave)"/><rect y="36" width="392" height="1" fill="#999"/></svg>
  <span class="track-time" style="left:132px">0:00</span><span class="track-time" style="left:508px">0:02</span>
  <div class="track-links"><a href="#">Download demo</a><a href="#">Share</a></div>
  <span class="price">0.99 c</span><a class="buy" href="#">Buy</a>
</div>

<!-- Footer -->
<footer class="site-footer">
  <a class="brand" href="#"><span class="brand-dot"></span>BRIDGET COLFER'S</a>
</footer>
<ul class="footer-col" style="left:465px;top:2688px">
  <li>Home</li><li>About me</li><li>Contact</li><li>Tour dates</li><li>Gallery</li><li>Store</li>
</ul>
<span class="footer-head" style="left:582px;top:2668px">Bridget Colfer Cruise:</span>
<ul class="footer-col light" style="left:582px;top:2684px">
  <li>Home</li><li>Artists</li><li>Prices</li><li>Flyer</li><li>Press</li><li>Contact</li><li>Booking</li>
</ul>
<span class="footer-head" style="left:844px;top:2668px">Conact:</span>
<div class="social"><span></span><span></span><span></span><span></span></div>
<span class="copyright">© 2015 - Company</span>

</body>
</html>
```